Wordpress Design Project (Dorvane)

We need a wordpress design for an established auction and real estate company based in New Jersey. The winning design will incorporate a professional color scheme and company logo in a clean layout.

Industry/Entity Type

Real Estate

Requirements
Must have
• - We will require winning designer to provide a layered PSD (Adobe photoshop) concept file, along with any non-standard font files used.

Logo attached. Will hopefully post better logo shortly. Please use site design colors of your choice as the logo is black & white. A site client mentions liking is http://www.plxbidhouse.example/. Homepage content will be an auction list as seen at http://www.ridgelinesaleindex.example/?page=5

Horizontal Navigation menu with these pages:
Home - Auction Calendar - Appraisals - Services - Company Profile - News & Events - Testimonials - Contact Us

A slideshow element on the home page using one of the placeholder images provided (or stock if higher resolution image is necessary).

Sidebar widgets to be included are: Email sign-up form - Featured Auctions - Testimonial widget - 'Our Videos' widget; Social media icons somewhere in layout (facebook, twitter, RSS, and Youtube)

Homepage content is text:
DORVANE OVERSIGHT COMPANY was founded 90 years ago in 1921 by Harold Dorvane, which makes us one of the oldest commercial and industrial auction and appraisal companies in America.

We have conducted thousands of auctions, assisting a wide range of companies both large and small achieve maximum value for their capital assets.
Nice to have
• - Site will have drop down menus, nice to have a sample look for them on one of the primary menu items.

```html
<!DOCTYPE html>
<html lang="en">
<head>
<meta charset="utf-8">
<title>Dorvane Oversight Co. – Auctioneers &amp; Appraisers</title>
<link href="https://fonts.googleapis.com/css2?family=Open+Sans:ital,wght@0,400;0,600;0,700;1,400&display=swap" rel="stylesheet">
<style>
:root{
  --dark:#2e2e2e;
  --dark-2:#444;
  --page:#ffffff;
  --line:#dedede;
  --bar:#efefef;
  --text:#555;
  --heading:#333;
  --orange:#e09a10;
  --orange-lt:#f7b52a;
  --footer:#3b3b3b;
}
*{margin:0;padding:0;box-sizing:border-box}
html,body{width:680px;height:1200px;overflow:hidden}
body{font-family:"Open Sans",sans-serif;background:var(--page);color:var(--text);position:relative}
.masthead{position:absolute;left:0;top:0;width:680px;height:216px;background:linear-gradient(#262626,#3d3d3d)}
.logo{position:absolute;left:38px;top:16px;width:142px;height:48px;background:#fff;border:2px solid #bbb;display:flex;align-items:center;justify-content:center;gap:6px;font-weight:700;font-size:15px;color:#111;letter-spacing:.5px}
.logo i{width:12px;height:12px;background:#111;display:block}
.social{position:absolute;left:552px;top:20px;display:flex;gap:6px}
.social span{width:18px;height:18px;border-radius:50%;display:block}
.search{position:absolute;left:480px;top:47px;width:162px;height:20px;border:1px solid #555;border-radius:3px;background:#2a2a2a;font-size:7px;font-style:italic;color:#888;padding:5px 8px}
.search b{position:absolute;right:0;top:0;width:18px;height:18px;border-left:1px solid #555}
.search b::after{content:"";position:absolute;left:7px;top:5px;border-left:4px solid #999;border-top:4px solid transparent;border-bottom:4px solid transparent}
.nav{position:absolute;left:37px;top:77px;width:606px;height:34px;background:linear-gradient(#fafafa,#e6e6e6);display:flex;border:1px solid #ccc}
.nav a{font-size:10px;color:#333;text-decoration:none;display:flex;align-items:center;padding:0 9.2px;border-right:1px solid #ccc;flex:0 0 auto}
.nav a:first-child{padding:0 14px}
.nav a:last-child{border:none;flex:1;justify-content:center}
.slider{position:absolute;left:36px;top:110px;width:608px;height:207px;background:#fff;border:1px solid #ddd}
.slide{position:absolute;left:3px;top:3px;width:602px;height:201px;background:linear-gradient(180deg,#9db8d8 0%,#c9d4df 30%,#b8323c 55%,#8e2028 80%,#5a5a5a 100%)}
.caption{position:absolute;left:3px;top:102px;width:225px;height:64px;background:rgba(40,40,40,.7);color:#fff;padding:10px 0 0 25px}
.caption h2{font-size:19px;font-weight:600;line-height:1.2}
.caption p{font-size:13px}
.arrows{position:absolute;right:12px;top:182px;color:#fff;font-size:14px}
.dots{position:absolute;left:268px;top:190px;width:62px;height:18px;background:var(--orange-lt);border-radius:10px 10px 0 0;display:flex;justify-content:center;align-items:center;gap:3px}
.dots i{width:5px;height:5px;border-radius:50%;background:#fff;display:block}
.welcome{position:absolute;left:38px;top:338px;width:405px}
.welcome h1{font-size:16px;font-weight:400;color:var(--heading);margin-bottom:6px}
.welcome h1 b{font-weight:700}
.welcome p{font-size:7.5px;line-height:14px;margin-bottom:4px}
.list-title{position:absolute;left:37px;top:443px;font-size:13px;font-weight:400;color:var(--heading)}
.auction{position:absolute;left:35px;width:408px;height:150px;border:1px solid var(--line);border-radius:3px}
.auction h3{height:29px;background:linear-gradient(#f7f7f7,#ececec);border-bottom:1px solid var(--line);font-size:11px;font-weight:400;color:#333;padding:6px 16px}
.auction .thumb{position:absolute;left:16px;top:37px;width:105px;height:98px;border:1px solid #e3e3e3;border-radius:3px}
.auction .info{position:absolute;left:133px;top:38px;font-size:6.5px;line-height:15px}
.auction .info h4{font-size:10px;font-weight:400;color:var(--orange);margin-bottom:1px}
.auction .info .type{font-size:8px;color:#333}
.btns{display:flex;gap:6px;margin-top:6px}
.btn{width:53px;height:17px;border-radius:2px;font-size:7px;color:#fff;display:flex;align-items:center;justify-content:center}
.btn.dark{background:linear-gradient(#555,#262626)}
.btn.orange{background:linear-gradient(#fbbf3c,#ef9a0f)}
.widget{position:absolute;left:468px;width:174px;border:1px solid var(--line);border-radius:3px;background:#fff}
.widget h3{height:30px;font-size:12px;font-weight:400;color:#333;padding:6px 15px;background:linear-gradient(#f9f9f9,#efefef);border-bottom:1px solid var(--line)}
.signup h3{background:linear-gradient(#f7b52a,#e39a0e);color:#fff;font-size:12px}
.signup p{font-size:8px;line-height:13px;padding:10px 16px 4px}
.field{margin:5px 16px 0 16px;height:17px;border:1px solid #ccc;border-radius:3px;font-size:6.5px;color:#777;padding:3px 8px}
.subscribe{position:absolute;right:16px;top:119px;width:59px;height:18px;background:linear-gradient(#555,#222);border-radius:3px;color:#fff;font-size:7px;display:flex;align-items:center;justify-content:center}
.feat{display:flex;gap:10px;padding:8px 0 0 15px;height:60px}
.feat .ph{width:38px;height:43px;flex:0 0 38px;border:1px solid #e3e3e3;border-radius:2px;margin-top:4px}
.feat div{font-size:6.5px;line-height:11px;color:#888}
.feat h5{font-size:8px;font-weight:400;color:var(--orange)}
.feat b{font-weight:400;color:#333}
.testi h3{background:linear-gradient(#4a4a4a,#1f1f1f);color:#fff}
.testi p{font-size:7px;line-height:13px;font-style:italic;color:#777;padding:8px 15px 4px}
.testi .by{font-style:normal;color:#444;font-size:7.5px;padding-top:0}
.video{position:absolute;left:8px;top:36px;width:158px;height:105px;background:linear-gradient(#3a2c22,#6b5a4e 60%,#a89888);border-radius:2px}
.video svg{position:absolute;left:67px;top:40px}
.footer{position:absolute;left:0;top:1118px;width:680px;height:82px;background:var(--footer)}
.footer nav{position:absolute;left:37px;top:18px;font-size:8px;color:#eee}
.footer nav span{margin:0 4px;color:#aaa}
.footer small{position:absolute;left:37px;top:39px;font-size:6px;color:#aaa}
.footer .fsocial{position:absolute;left:592px;top:20px;display:flex;gap:3px}
.footer .fsocial i{width:14px;height:14px;border-radius:2px;display:block}
</style>
</head>
<body>
<header class="masthead">
  <div class="logo"><i></i>DORVANE</div>
  <div class="social" aria-label="Social links">
    <span style="background:#3b5998"></span><span style="background:#2fb7ea"></span><span style="background:#ddd"></span><span style="background:#f08a1d"></span>
  </div>
  <div class="search">Search here..<b></b></div>
  <nav class="nav">
    <a>Home</a><a>Auction Calendar</a><a>Appraisals</a><a>Services</a><a>Company Profile</a><a>News &amp; Events</a><a>Testimonials</a><a>Contact Us</a>
  </nav>
  <div class="slider">
    <div class="slide" role="img" aria-label="Photo of a row of red semi trucks lined up for auction"></div>
    <div class="caption"><h2>Auctions &amp; Appraisers</h2><p>Nunc tempus felis vitae urna</p></div>
    <div class="arrows">‹ ›</div>
    <div class="dots"><i></i><i></i><i></i><i></i></div>
  </div>
</header>

<section class="welcome">
  <h1>WELCOME TO <b>DORVANE OVERSIGHT CO.</b></h1>
  <p>DORVANE OVERSIGHT COMPANY was founded 90 years ago in 1921 by Harold Dorvane, which makes us one of the oldest commercial and industrial auction and appraisal companies in America.</p>
  <p>We have conducted thousands of auctions, assisting a wide range of companies both large and small achieve maximum value for their capital assets.</p>
</section>

<h2 class="list-title">LIST OF OUR AUCTIONS</h2>

<article class="auction" style="top:466px">
  <h3>Nunc tempus felis vitae urna</h3>
  <div class="thumb" role="img" aria-label="Photo of a dark wooden office desk" style="background:linear-gradient(135deg,#6b5a4e,#2b211c)"></div>
  <div class="info"><h4>Mauris vel lacus vitae felis</h4><div class="type">Live On-Site Auction</div><div>Begins:&nbsp; Saturday, August 10, 2013 at 10:00 AM EDT</div><div>Location: 42 Marlow Yard Fenwick, VA 24099</div><div class="btns"><span class="btn dark">DETAILS</span><span class="btn orange">PHOTOS</span></div></div>
</article>
<article class="auction" style="top:627px">
  <h3>Praesent elementum elit at tellus</h3>
  <div class="thumb" role="img" aria-label="Photo of a wooden and red designer table" style="background:linear-gradient(135deg,#b13a30,#8a6a48)"></div>
  <div class="info"><h4>Mauris vel lacus vitae felis</h4><div class="type">Live On-Site Auction</div><div>Begins:&nbsp; Saturday, August 10, 2013 at 10:00 AM EDT</div><div>Location: 42 Marlow Yard Fenwick, VA 24099</div><div class="btns"><span class="btn dark">DETAILS</span><span class="btn orange">PHOTOS</span></div></div>
</article>
<article class="auction" style="top:788px">
  <h3>Consectetuer adipiscing elit</h3>
  <div class="thumb" role="img" aria-label="Photo of a pair of carved antique chairs with a side table" style="background:linear-gradient(#fff,#d8d2cc)"></div>
  <div class="info"><h4>Mauris vel lacus vitae felis</h4><div class="type">Live On-Site Auction</div><div>Begins:&nbsp; Saturday, August 10, 2013 at 10:00 AM EDT</div><div>Location: 42 Marlow Yard Fenwick, VA 24099</div><div class="btns"><span class="btn dark">DETAILS</span><span class="btn orange">PHOTOS</span></div></div>
</article>
<article class="auction" style="top:949px">
  <h3>Lorem ipsum dolor sit amet</h3>
  <div class="thumb" role="img" aria-label="Photo of a wooden bed frame with white bedding" style="background:linear-gradient(#fff,#e2d6c8)"></div>
  <div class="info"><h4>Mauris vel lacus vitae felis</h4><div class="type">Live On-Site Auction</div><div>Begins:&nbsp; Saturday, August 10, 2013 at 10:00 AM EDT</div><div>Location: 42 Marlow Yard Fenwick, VA 24099</div><div class="btns"><span class="btn dark">DETAILS</span><span class="btn orange">PHOTOS</span></div></div>
</article>

<aside>
  <section class="widget signup" style="top:334px;height:150px">
    <h3>EMAIL SIGN-UP FORM</h3>
    <p>Please subscribe here for latest news and Offers</p>
    <div class="field">username</div>
    <div class="field">email address</div>
    <span class="subscribe">SUBSCRIBE</span>
  </section>
  <section class="widget" style="top:494px;height:207px">
    <h3>Featured Auctions</h3>
    <div class="feat"><span class="ph" role="img" aria-label="Photo of wooden cabinets" style="background:#c89a5e"></span><div><h5>Auction Name</h5>Nunc tempus felis vitae urna Vivamus porttitor<br><b>LEARN MORE</b></div></div>
    <div class="feat"><span class="ph" role="img" aria-label="Photo of a conference table" style="background:#7a5040"></span><div><h5>Auction Name</h5>Nunc tempus felis vitae urna Vivamus porttitor<br><b>LEARN MORE</b></div></div>
    <div class="feat"><span class="ph" role="img" aria-label="Photo of an office interior" style="background:#b89a80"></span><div><h5>Auction Name</h5>Nunc tempus felis vitae urna Vivamus porttitor<br><b>LEARN MORE</b></div></div>
  </section>
  <section class="widget testi" style="top:731px;height:132px">
    <h3>Testimonials</h3>
    <p>Phasellus felis dolor, scelerisque a, tempus eget, lobortis id, libero. Donec scelerisque leo ac risus. Praesent sit amet est. In dictum, dolor eu dictum porttitor enim felis viverra mi, eget luctus massa purus quis odio</p>
    <p class="by">By Author Name</p>
  </section>
  <section class="widget" style="top:872px;height:151px">
    <h3>Our Videos</h3>
    <div class="video" role="img" aria-label="Video still of an auction room with an audience and auctioneer">
      <svg width="24" height="24" viewBox="0 0 24 24"><circle cx="12" cy="12" r="10.5" fill="rgba(0,0,0,.4)" stroke="#fff" stroke-width="1.5"/><path d="M9.5 7.5 17 12l-7.5 4.5z" fill="#fff"/></svg>
    </div>
  </section>
</aside>

<footer class="footer">
  <nav>Home<span>|</span>Auction Calendar<span>|</span>Appraisals<span>|</span>Services<span>|</span>Company Profile<span>|</span>News &amp; Events<span>|</span>Testimonials<span>|</span>Contact Us</nav>
  <small>Copyright © 2013 Company Name.&nbsp; All right reserved.&nbsp; Term of Use</small>
  <div class="fsocial"><i style="background:#2fa6d8"></i><i style="background:#2a7ab8"></i><i style="background:#3b5998"></i></div>
</footer>
</body>
</html>
```